For Sale Poster Design

We need a beautiful and tropical looking FOR SALE poster for our speed boat.

Poster format need to be 297x420mm / 300dpi
PSD with all layers.

The photos from the boat can be downloaded here: www.korvado.nl/photos.zip

Target Market(s)

Tourists, expats

Requirements
Must have
• The poster need to have the following text:

Speed Boat Sale

This beautiful full glass fiber speedboat (location Lombok, Indonesia) is perfect for tropical conditions: island transfer, diving, wake boarding, fishing, private charters and leisure activities.

The newly bought 2x 200 HP TORUMI 4 Stroke (2013) will give you an enormous power on the water with maximum speed of 40 Knot / 74 Km/hour. This will bring you from Lombok to Bali in just 50 minutes and only few minutes long from the famous tropical Gili islands.

The speedboat also has the comfort of a small cabin with skylight, sun controlled ventilation system, a small bed, a toilet and a fridge. There are 16 seats in the open section of the boat. The boat is equipped with modern brand-new GPS, Sonar and an FM / AM Radio system.

This speedboat was built in 2011 and is meticulously maintained to the highest standard. It comes with a captain and boatman.

Specs:
Overall length: 11 Meter 36 feet.
Built year: 2011, Bali
Engines: 2x 200 HP TORUMI 4 Stroke (Bought 2013)
Capacity: Max. 16 People (Incl. Crew)
Max speed: 40 Knot / 74 Km/hour
GPS / Sonar: Pelcorn RM-42TX
Tankage: 300 Liter
Lighting: LED / Halogen

Price 99.000 USD
Nice to have
• Big FOR SALE banner on the poster

```html
<!DOCTYPE html>
<html lang="en">
<head>
<meta charset="utf-8">
<title>Speed Boat For Sale Poster</title>
<link href="https://fonts.googleapis.com/css2?family=Anton&family=Arimo:wght@400;700&display=swap" rel="stylesheet">
<style>
  :root {
    --banner-yellow: #fff200;
    --sale-red: #c8161d;
    --sale-red-dark: #8e0c10;
    --sale-red-light: #e8383d;
    --ribbon-yellow: #f4d90a;
    --ocean-deep: #0d4f9a;
    --ocean-mid: #2a7fcf;
    --ocean-light: #6fb6ea;
    --lagoon: #3fd1b0;
    --sand: #f2e6c8;
    --sky: #4c9be0;
    --row-red: #c4161c;
    --row-line: #f3c9ca;
    --white: #ffffff;
    --text-shadow: rgba(0, 20, 60, 0.55);
  }
  * { margin: 0; padding: 0; box-sizing: border-box; }
  html, body { width: 848px; height: 1200px; overflow: hidden; background: #ffffff; }
  .poster {
    position: relative;
    width: 848px;
    height: 1200px;
    overflow: hidden;
    font-family: "Arimo", Arial, sans-serif;
    color: var(--white);
  }
  .top-band {
    position: absolute; left: 0; top: 0; width: 848px; height: 172px;
    background: var(--banner-yellow);
  }
  .beach-scene {
    position: absolute; left: 0; top: 172px; width: 848px; height: 358px;
    background: linear-gradient(180deg, var(--sky) 0%, #9fd0f3 38%, var(--lagoon) 60%, #7fe3cf 78%, var(--sand) 100%);
  }
  .headline {
    position: absolute; left: 0; top: 0; width: 848px; height: 260px;
    filter: drop-shadow(3px 5px 4px rgba(0,0,0,0.45));
  }
  .ocean-backdrop {
    position: absolute; left: 0; top: 530px; width: 848px; height: 670px;
    background: linear-gradient(180deg, var(--ocean-light) 0%, var(--ocean-mid) 35%, var(--ocean-deep) 100%);
  }
  .rope-band {
    position: absolute; left: 0; top: 530px; width: 848px; height: 46px;
    background: linear-gradient(180deg, rgba(255,255,255,0.0), rgba(255,255,255,0.25), rgba(255,255,255,0.0));
  }
  .ribbon {
    position: absolute; left: 24px; top: 524px; width: 230px; height: 165px;
  }
  .ribbon-text {
    position: absolute; left: 58px; top: 536px; width: 180px;
    transform: rotate(-9deg);
    font-family: "Anton", Impact, sans-serif;
    font-size: 33px; line-height: 38px;
    text-align: center; text-transform: uppercase;
    color: var(--white);
    font-style: italic;
    text-shadow: 2px 2px 3px rgba(0,0,0,0.4);
  }
  .interior-photo {
    position: absolute; left: 436px; top: 512px; width: 396px; height: 228px;
    transform: rotate(4deg);
    background: var(--white);
    padding: 8px;
    box-shadow: 3px 4px 8px rgba(0,0,0,0.4);
  }
  .interior-photo .fill {
    width: 100%; height: 100%;
    background: linear-gradient(180deg, #dfe7ea 0%, #f4f1ea 40%, #d9c39a 75%, #f0ece4 100%);
  }
  .body-copy {
    position: absolute; left: 31px; top: 712px; width: 390px;
    font-size: 16px; line-height: 19.5px;
    text-align: justify;
    hyphens: auto;
    text-shadow: 1px 1px 2px var(--text-shadow);
  }
  .body-copy p { margin-bottom: 26px; }
  .spec-title {
    position: absolute; left: 455px; top: 801px; width: 370px;
    text-align: center;
    font-size: 18.5px; letter-spacing: 0.3px;
    text-shadow: 1px 1px 2px var(--text-shadow);
  }
  .spec-table {
    position: absolute; left: 458px; top: 836px; width: 369px;
    border-collapse: collapse;
    font-size: 16.5px;
    box-shadow: 2px 3px 6px rgba(0,0,0,0.35);
  }
  .spec-table td {
    background: linear-gradient(180deg, var(--sale-red-light) 0%, var(--row-red) 45%, var(--sale-red-dark) 100%);
    border: 1px solid var(--row-line);
    padding: 0 8px;
    line-height: 19px;
  }
  .spec-table .label { width: 148px; text-align: right; }
  .spec-table .value { padding-left: 12px; }
  .price {
    position: absolute; left: 455px; top: 1158px; width: 330px;
    text-align: center; font-size: 15px;
    text-shadow: 1px 1px 2px var(--text-shadow);
  }
</style>
</head>
<body>
<div class="poster">
  <div class="top-band"></div>
  <div class="beach-scene" role="img" aria-label="Photo of the white speedboat with twin outboard engines moored in a turquoise tropical lagoon beside a sandy beach, rocks and palm trees"></div>

  <svg class="headline" viewBox="0 0 848 260" aria-label="For Sale">
    <defs>
      <linearGradient id="saleRed" x1="0" y1="0" x2="0" y2="1">
        <stop offset="0" stop-color="#ee3b40"/>
        <stop offset="0.5" stop-color="#c8161d"/>
        <stop offset="1" stop-color="#8e0c10"/>
      </linearGradient>
    </defs>
    <text x="22" y="248" textLength="808" lengthAdjust="spacingAndGlyphs"
          font-family="Anton, Impact, sans-serif" font-size="290"
          fill="url(#saleRed)" stroke="#ffffff" stroke-width="3">FOR SALE</text>
  </svg>

  <div class="ocean-backdrop" role="img" aria-label="Photo of open blue sea with a speedboat wake"></div>
  <div class="rope-band" role="img" aria-label="Row of life rings on a rope"></div>

  <svg class="ribbon" viewBox="0 0 230 165" aria-hidden="true">
    <polygon points="6,42 34,40 34,160" fill="var(--ribbon-yellow)"/>
    <polygon points="24,30 208,4 224,92 40,122" fill="var(--sale-red)" stroke="var(--sale-red-dark)" stroke-width="2" stroke-linejoin="round"/>
  </svg>
  <div class="ribbon-text">Speed Boat<br>Sale</div>

  <div class="interior-photo">
    <div class="fill" role="img" aria-label="Photo of the boat's open seating area with beige cushioned benches and the helm"></div>
  </div>

  <div class="body-copy">
    <p>This beautiful full glass fiber speedboat (location Lombok, Indonesia) is perfect for tropical conditions: island transfer, diving, wake boarding, fishing, private charters and leisure activities.</p>
    <p>The newly bought 2x 200 HP TORUMI 4 Stroke (2013) will give you an enormous power on the water with maximum speed of 40 Knot / 74 Km/hour. This will bring you from Lombok to Bali in just 50 minutes and only few minutes long from the famous tropical Gili islands.</p>
    <p>The speedboat also has the comfort of a small cabin with skylight, sun controlled ventilation system, a small bed, a toilet and a fridge. There are 16 seats in the open section of the boat. The boat is equipped with modern brand-new GPS, Sonar and an FM / AM Radio system</p>
    <p>This speedboat was built in 2011 and is meticulously maintained to the highest standard. It comes with a captain and boatman.</p>
  </div>

  <div class="spec-title">SPECIFICATION</div>
  <table class="spec-table">
    <tr style="height:30px"><td class="label">Overall length:</td><td class="value">11 Meter 36 feet.</td></tr>
    <tr style="height:32px"><td class="label">Built Year:</td><td class="value">2011, Bali</td></tr>
    <tr style="height:60px"><td class="label">Engines:</td><td class="value">2x 200 HP TORUMI<br>4 Stroke (Bought 2013)</td></tr>
    <tr style="height:58px"><td class="label">Capacity:</td><td class="value">Max. 16 People<br>(Incl. Crew)</td></tr>
    <tr style="height:30px"><td class="label">Max speed:</td><td class="value">40 Knot / 74 Km/hour</td></tr>
    <tr style="height:32px"><td class="label">GPS / Sonar:</td><td class="value">Pelcorn RM-42TX</td></tr>
    <tr style="height:30px"><td class="label">Tankage:</td><td class="value">300 Liter</td></tr>
    <tr style="height:30px"><td class="label">Lighting:</td><td class="value">LED / Halogen</td></tr>
  </table>

  <div class="price">Price 99.000 USD</div>
</div>
</body>
</html>
```